Skin cancer clinic services trifold brochure

Need trifold brochure listing skin cancer services our clinic provides, staff information, location and brief about skin cancer with colours similar to our web site www.Lumorava.clinic. I will provide more information regarding services and staff but want this colourful and standout as it will be given to other referring doctors or patients

Target Market(s)

Age 40 to 80 years

Industry/Entity Type

Medical

Font styles to use
Serif

Colors

Designer to choose colors to be used in the design.

Requirements
Must have
• Logo, services, contact info, beach or sun look and colours similar to web site or logo

```html
<!DOCTYPE html>
<html lang="en">
<head>
<meta charset="utf-8">
<title>Lumorava Skin Cancer Clinic – Brochure</title>
<link href="https://fonts.googleapis.com/css2?family=Tinos:ital,wght@0,400;0,700;1,700&display=swap" rel="stylesheet">
<style>
:root{
  --gold:#e8d4a2;
  --navy:#0c4876;
  --ink:#1a1a1a;
  --white:#ffffff;
  --link:#d81e1e;
  --badge:#4a3c97;
}
*{margin:0;padding:0;box-sizing:border-box}
html,body{width:1200px;height:848px;overflow:hidden;background:var(--white)}
body{font-family:"Tinos","Times New Roman",serif;color:var(--ink);font-size:12.6px;line-height:14.3px}
.brochure{position:relative;width:1200px;height:848px}
.panel{position:absolute;top:0;height:848px}
.panel--left{left:0;width:407px}
.panel--middle{left:407px;width:386px;background:var(--navy)}
.panel--right{left:793px;width:407px}
.band{position:absolute;left:0;right:0;background:var(--gold);color:var(--white);font-weight:700;text-transform:uppercase;letter-spacing:.5px}
.band h2{font-size:25px;line-height:22px;padding-left:20px}
.photo{position:absolute}

.fact-band{top:0;height:41px}
.fact-band h2{padding-top:10px}
.question{position:absolute;left:294px;top:-14px;font-size:215px;line-height:200px;font-weight:700;color:#000}
.facts{position:absolute;left:20px;top:60px;width:278px}
.facts em{font-weight:700}
.photo--treatment{left:0;top:194px;width:407px;height:235px;background:linear-gradient(120deg,#e9e6df 0%,#c9c2b5 40%,#5aa8c8 80%,#3c88b0 100%)}
.about-band{top:446px;height:42px}
.about-band h2{padding-top:12px}
.badge{position:absolute;left:22px;top:502px;width:136px;height:192px;background:var(--badge)}
.pattern-area{position:absolute;left:18px;top:704px;width:140px;height:144px;background:linear-gradient(160deg,#f6f6f6 0%,#fbfbfb 100%)}
.about{position:absolute;left:167px;top:499px;width:224px}
.about p{margin-bottom:14.3px}
.about a{color:var(--link);font-weight:700;text-decoration:none}

.photo--reception{left:12px;top:0;width:361px;height:166px;background:linear-gradient(100deg,#d9d8d6 0%,#eeeeec 45%,#c8c6c2 100%)}
.staff-band{top:178px;height:41px}
.staff-band h2{font-size:26px;padding-top:10px;color:#111}
.staff{position:absolute;left:20px;top:228px;width:354px;color:var(--white);font-weight:700}
.staff-intro{margin-bottom:18px}
.doctors{list-style:none}
.doctors li{position:relative;padding-left:11px;line-height:20px;margin-bottom:4.5px}
.doctors li::before,.services li::before{content:"";position:absolute;left:0;top:5px;width:7px;height:7px;background:var(--gold)}
.staff-outro{margin-top:8px}
.photo--storefront{left:12px;top:567px;width:361px;height:281px;background:linear-gradient(180deg,#9aa0a6 0%,#b7bcc0 40%,#4f5153 45%,#6b6c6b 60%,#dad7d0 100%)}

.services-band{top:0;height:63px}
.services-band h2{padding-top:9px;font-size:25px;line-height:22px}
.services{position:absolute;left:822px;width:362px;list-style:none;font-size:12.8px}
.services li{position:relative;padding-left:12px;margin-bottom:10px}
.services li::before{top:3px}
.services b{font-weight:700}
.services--top{top:77px}
.services--bottom{top:545px}
.photo--room{left:29px;top:363px;width:378px;height:163px;background:linear-gradient(100deg,#c8cbce 0%,#e6e5e2 50%,#b9a88c 100%)}
</style>
</head>
<body>
<main class="brochure">

  <section class="panel panel--left">
    <div class="band fact-band"><h2>Did you know</h2></div>
    <div class="question" aria-hidden="true">?</div>
    <p class="facts">Skin Cancers account for 80% of all newly diagnosed cancers with two in three Australians diagnosed with skin cancer by the time they are 70.&nbsp; Although over 90% of skin cancers are due to over exposure to UV light, some are caused by chemical exposure or are hereditary. Over 2000 Australians die from skin cancer each year.<br><em>Have you had your skin checked lately?</em></p>
    <div class="photo photo--treatment" role="img" aria-label="Photo of a nurse treating a patient in a treatment room with a beach scene projected on the wall"></div>

    <div class="band about-band"><h2>About us</h2></div>
    <div class="badge" role="img" aria-label="Accreditation badge"></div>
    <div class="pattern-area" role="img" aria-label="Faint decorative pattern"></div>
    <div class="about">
      <p>Lumorava Skin Cancer Clinic is a purpose-built skin cancer clinic dedicated to providing the highest-level patient care to the Central Coast community and surrounding regions.&nbsp; Our skilled doctors and nurses have extensive experience and advanced training in Skin Cancer Medicine in order to provide quality care to our patients.&nbsp; We specialise in a comprehensive approach to skin with preventive skin cancer care, expert diagnostic dermoscopy skills highlighting artificial intelligent analytics, and definitive surgical and medical treatments of skin cancers.</p>
      <p>Skin cancer medicine is all we do.</p>
      <p>We welcome you to “virtually” walk through our clinic at <a href="#">www.Lumorava.clinic</a></p>
    </div>
  </section>

  <section class="panel panel--middle">
    <div class="photo photo--reception" role="img" aria-label="Photo of the clinic reception desk and corridor"></div>
    <div class="band staff-band"><h2>Our Staff</h2></div>
    <div class="staff">
      <p class="staff-intro">At Lumorava Skin Cancer Clinic, our highly qualified administrative staff, nurses and doctors are an integral part of the team ensuring excellent clinical care is provided to our patients.&nbsp; We currently have 5 experienced local doctors:</p>
      <ul class="doctors">
        <li>Dr. Marina Castell, BMed, FRACGP, Diploma Skin Cancer Medicine/Surgery, Diploma Aesthetic Medicine</li>
        <li>Dr. Renata Voss, BMed, FRACGP, Diploma Skin Cancer Medicine/Surgery</li>
        <li>Dr. Helen Ashcombe, MBBS, FRACGP</li>
        <li>Dr. Tom Whitfield, MBBS (Syd), Dip Law</li>
        <li>Dr. Kate Dunmore, MBBS (Hons), FRACGP, Cert. Skin Cancer Medicine</li>
      </ul>
      <p class="staff-outro">Early detection of skin cancers is vital for the best outcome. Lumorava has invested in technology and research to provide the latest diagnostic services and treatments to meet the needs of our patients.</p>
    </div>
    <div class="photo photo--storefront" role="img" aria-label="Photo of the clinic shopfront with its web address on the awning"></div>
  </section>

  <section class="panel panel--right">
    <div class="band services-band"><h2>Professional Skin<br>Services</h2></div>
    <div class="photo photo--room" role="img" aria-label="Photo of a nurse examining a patient's arm in a consulting room"></div>
  </section>

  <ul class="services services--top">
    <li>Advanced Skin Cancer Detection with detailed Full Body skin checks using dermoscopy and technology to minimise unnecessary excisions.</li>
    <li><b>Individual Mole mapping and full body photography utilising intelligent skin analytics with DermaTrace –</b> an artificial intelligence-powered platform which provides tools for documenting and diagnosing skin cancers and evidence-based care. Powered by AI algorithms, it will identify changes to the skin over time and support early clinical decisions and diagnosis.</li>
    <li><b>SpotView Skin Imaging System which captures high-quality images using LayerScan –</b> clinically proven technology which provides a unique level of detail and information from up to 2mm beneath the skin’s surface allowing deeper assessment and risk of melanoma.</li>
    <li>Purpose Built Skin Cancer Facility providing Surgical treatments in 2 dedicated fully equipped theatres and Treatment room staffed by skilled skin cancer medicine nurses</li>
  </ul>
  <ul class="services services--bottom">
    <li>Large referral basis for our patients that may require extensive therapy for their skin cancers, including Radiotherapy for cosmetically sensitive areas that are not optimally treated with surgery, Advanced care under the Melanoma Unit Harbourside or MOHs Surgery and more.</li>
    <li><b>Priority Spot Checks –</b> appointments are set aside every day for urgent suspicious lesions allowing for quick evaluation, whether for an existing or new patient.&nbsp; Although we welcome GP referrals, it is not required.</li>
    <li><b>GP Team Approach –</b> Lumorava believes it is important that an integrated team approach to a patient’s skin cancer care is important, and communication of histological results and findings are shared with their GP upon permission.</li>
    <li><b>Pain minimisation Techniques –</b>Topical numbing creams and ChillPoint numbing agents are available to minimise tenderness that can come with local anaesthetics. Our theatres are equipped with overhead projectors playing calming nature scenes to ensure our patients are comfortable.</li>
  </ul>

</main>
</body>
</html>
```